BrightKeel Business Card Contest

We are looking for a modern business card that catches attention and is unique. Attached is the brand guide and logo files. Please note that the back side (not the side with our name and info) with be UV raise printed, so have fun with the design there. We want to include Name, Title, Phone number, email, website.

Contact Information for Business Card

Please see project description

```html
<!DOCTYPE html>
<html lang="en">
<head>
<meta charset="utf-8">
<title>BrightKeel Business Card</title>
<link href="https://fonts.googleapis.com/css2?family=Montserrat:wght@400;500;700&display=swap" rel="stylesheet">
<style>
  :root {
    --backdrop: #4a4a4a;
    --card-black: #1d1d1d;
    --uv-ink: #2e2e2e;
    --card-white: #ffffff;
    --ink: #1b1b24;
    --navy: #1f3a7a;
    --orange: #ee7d22;
    --icon-blue: #3fa9dc;
  }
  * { margin: 0; padding: 0; box-sizing: border-box; }
  html, body {
    width: 1200px; height: 875px; overflow: hidden;
    background: var(--backdrop);
    font-family: "Montserrat", sans-serif;
  }
  .sheet {
    width: 1200px; height: 875px;
    display: flex; flex-direction: column; align-items: center; justify-content: center;
    gap: 44px;
  }
  .card {
    width: 640px; height: 366px;
    border-radius: 22px;
    position: relative; overflow: hidden;
  }
  /* Back side */
  .card-back { background: var(--card-black); }
  .card-back .brand {
    position: absolute; left: 50%; top: 50%; transform: translate(-50%, -50%);
    display: flex; align-items: center; gap: 18px;
  }
  .brand-square { width: 40px; height: 40px; background: var(--orange); }
  .card-back .brand-name {
    font-size: 64px; font-weight: 500; color: var(--uv-ink); letter-spacing: -1px;
  }
  /* Front side */
  .card-front { background: var(--card-white); }
  .card-front .brand-name {
    position: absolute; left: 62px; top: 78px;
    font-size: 54px; font-weight: 500; color: var(--ink); letter-spacing: -1px;
  }
  .identity-mark {
    position: absolute; left: 40px; top: 178px;
    width: 16px; height: 40px; background: var(--orange);
  }
  .person { position: absolute; left: 74px; top: 172px; }
  .person-name { font-size: 24px; font-weight: 700; color: var(--navy); letter-spacing: 0.5px; }
  .person-title { font-size: 14px; font-weight: 400; color: var(--ink); margin-top: 2px; }
  .contacts {
    position: absolute; left: 74px; top: 244px;
    list-style: none; display: flex; flex-direction: column; gap: 7px;
  }
  .contact { display: flex; align-items: center; gap: 10px; font-size: 14px; color: var(--ink); }
  .contact svg { width: 14px; height: 14px; flex: none; }
  .edge-band {
    position: absolute; left: 0; bottom: 0; width: 640px; height: 16px;
    background: var(--navy);
  }
</style>
</head>
<body>
<main class="sheet">
  <section class="card card-back" aria-label="Card back">
    <div class="brand">
      <span class="brand-square"></span>
      <span class="brand-name">BrightKeel</span>
    </div>
  </section>

  <section class="card card-front" aria-label="Card front">
    <div class="brand-name">BrightKeel</div>
    <span class="identity-mark"></span>
    <div class="person">
      <div class="person-name">DANA WHITLOW</div>
      <div class="person-title">CEO/Founder</div>
    </div>
    <ul class="contacts">
      <li class="contact">
        <svg viewBox="0 0 16 16" aria-hidden="true"><path fill="var(--icon-blue)" d="M3.5 1.5l2.5 3-1.6 1.6a8 8 0 0 0 5.5 5.5L11.5 10l3 2.5-1.5 2.2C7.5 15 1 8.5 1.3 3z"/></svg>
        <span>(555) 214-7730</span>
      </li>
      <li class="contact">
        <svg viewBox="0 0 16 16" aria-hidden="true"><rect x="1" y="3" width="14" height="10" rx="1.5" fill="var(--icon-blue)"/><path d="M1.5 4l6.5 5 6.5-5" fill="none" stroke="#fff" stroke-width="1.4"/></svg>
        <span>info@brightkeel.com</span>
      </li>
      <li class="contact">
        <svg viewBox="0 0 16 16" aria-hidden="true"><circle cx="8" cy="8" r="7" fill="var(--icon-blue)"/><path d="M1 8h14M8 1c-3 3.5-3 10.5 0 14M8 1c3 3.5 3 10.5 0 14" fill="none" stroke="#fff" stroke-width="1"/></svg>
        <span>www.brightkeel.com</span>
      </li>
    </ul>
    <div class="edge-band" role="img" aria-label="Coloured edge band along the bottom of the card"></div>
  </section>
</main>
</body>
</html>
```